Publisher needs a book cover design for ‘Lanterns Over the Marsh Gate’ book

We need a book cover (front, back, spine) for the 2nd edition of a book entitled ‘Lanterns Over the Marsh Gate’ and subtitled ‘the quiet geography of tidal winds, ferry routes and harbour lanterns’ (inverted commas not to be part of the title and subtitle). The author is Rupert Calloway. The publisher is Vellmark Press. The finished size of the paperback version will be the industry standard 9" x 6". There will be paperback, hardback, and e-book versions. The final number of pages is expected to be in the region 150-180 pages. Text for the back cover is not yet available, but at the bottom of the back cover should be publisher logo (rectangular) on the left and space for the ISBN bar code on the right. The circular logo should be on the spine. The design should be original and not include any stock images that have been created by someone else or may require obtaining a copyright licence to use. Symbols in common use and not copyrighted are probably ok. There are no required images, photographs or symbols except the publisher logo at the left bottom of the back cover and lower spine. Spine lettering should be UK/US style with the top of the writing nearest the front cover. The designer is free to be creative using appropriate diagrams, symbols or abstract designs. Rectangular and circular variants of the publisher logo are attached. Designers are assured that when evaluating designs absolutely no notice whatsoever is taken of a designer's Pixo Rally ranking or status; We are completely output driven, so what matters is the design, not the ranking or status of the designer. In a similar way, designs are not evaluated as 'good' or 'bad' - the winning design will be chosen after review by a design review panel and is not decided arbitrarily by a single person. All submitted designs should be capable of effective copyright assignment.

Target Market(s)

Practitioners, parents, teachers, pupils and academics concerned with child protection, safeguarding and the elimination of emotional abuse of children in the classroom

Font styles to use
Serif
Sans Serif

Requirements
Must have
• • Title, author, edition, subtitle, publisher logo
Nice to have
• • Originality, innovation
Should not have
• • Stock images or anything else requiring additional copyright discussions and negotiations.

```html
<!DOCTYPE html>
<html lang="en">
<head>
<meta charset="utf-8">
<title>Lanterns Over the Marsh Gate — Cover</title>
<link rel="stylesheet" href="https://fonts.googleapis.com/css2?family=Bodoni+Moda:opsz,wght@6..96,400;6..96,700&display=swap">
<style>
  :root {
    --paper: #ffffff;
    --ink: #000000;
    --night: #0b0b1a;
    --corridor-blue: #3a4a8a;
    --corridor-light: #e8ecf5;
    --corridor-mid: #7d6a7a;
  }
  html, body {
    margin: 0;
    padding: 0;
    overflow: hidden;
    background: var(--paper);
  }
  .cover {
    position: relative;
    width: 1200px;
    height: 880px;
    background: var(--paper);
    color: var(--ink);
    font-family: "Bodoni Moda", "Bodoni 72", Didot, serif;
    font-weight: 400;
    overflow: hidden;
  }
  .back-title, .front-title {
    position: absolute;
    margin: 0;
    font-weight: 400;
    line-height: 1.04;
    letter-spacing: -0.5px;
  }
  .back-title {
    left: 48px;
    top: 34px;
    font-size: 64px;
  }
  .back-blurb {
    position: absolute;
    left: 45px;
    top: 290px;
    width: 510px;
    margin: 0;
    font-size: 16.6px;
    line-height: 26.8px;
    text-align: justify;
    hyphens: auto;
  }
  .back-publisher {
    position: absolute;
    left: 50px;
    top: 776px;
    display: flex;
    align-items: center;
    gap: 8px;
    font-size: 22px;
    letter-spacing: 1px;
  }
  .publisher-dot {
    width: 40px;
    height: 40px;
    border-radius: 50%;
    background: var(--ink);
  }
  .isbn-space {
    position: absolute;
    left: 367px;
    top: 728px;
    width: 193px;
    height: 115px;
    background: var(--ink);
  }
  .spine-title, .spine-edition, .spine-author {
    position: absolute;
    writing-mode: vertical-rl;
    white-space: nowrap;
  }
  .spine-title {
    left: 581px;
    top: 46px;
    font-size: 24px;
  }
  .spine-edition {
    left: 586px;
    top: 470px;
    font-size: 15px;
  }
  .spine-author {
    left: 583px;
    top: 622px;
    font-size: 20px;
    font-weight: 700;
  }
  .spine-publisher {
    position: absolute;
    left: 584px;
    top: 796px;
    width: 24px;
    height: 24px;
    border-radius: 50%;
    background: var(--ink);
  }
  .spine-publisher-name {
    position: absolute;
    left: 574px;
    top: 824px;
    width: 44px;
    text-align: center;
    font-size: 6px;
    letter-spacing: 0.5px;
  }
  .front-art {
    position: absolute;
    left: 616px;
    top: 0;
    width: 584px;
    height: 347px;
  }
  .front-title {
    left: 646px;
    top: 384px;
    font-size: 66px;
  }
  .front-subtitle {
    position: absolute;
    left: 648px;
    top: 630px;
    margin: 0;
    font-size: 20.5px;
    line-height: 26px;
  }
  .front-edition {
    position: absolute;
    left: 648px;
    top: 716px;
    margin: 0;
    font-size: 18px;
    letter-spacing: 1px;
  }
  .front-author {
    position: absolute;
    left: 648px;
    top: 816px;
    margin: 0;
    font-size: 29px;
    font-weight: 700;
  }
</style>
</head>
<body>
<div class="cover">
  <section class="back-cover">
    <h2 class="back-title">Lanterns<br>Over the Marsh<br>Gate</h2>
    <p class="back-blurb">Lorem Ipsum is simply dummy text of the printing and typesetting industry. Lorem Ipsum has been the industry's standard dummy text ever since the 1500s, when an unknown printer took a galley of type and scrambled it to make a type specimen book. It has survived not only five centuries, but also the leap into electronic typesetting, remaining essentially unchanged. It was popularised in the 1960s with the release of Tracemark sheets containing Lorem Ipsum passages, and more recently with desktop publishing software like Quillset Layout including versions of Lorem Ipsum.</p>
    <div class="back-publisher"><span class="publisher-dot"></span><span>VELLMARK PRESS</span></div>
    <div class="isbn-space"></div>
  </section>

  <section class="spine">
    <div class="spine-title">Lanterns Over the Marsh Gate</div>
    <div class="spine-edition">2nd edition</div>
    <div class="spine-author">Rupert Calloway</div>
    <div class="spine-publisher"></div>
    <div class="spine-publisher-name">VELLMARK</div>
  </section>

  <section class="front-cover">
    <svg class="front-art" role="img" aria-label="Glowing, high-contrast view down a long corridor lined with doors, vanishing into darkness" viewBox="0 0 584 347" preserveAspectRatio="none">
      <defs>
        <linearGradient id="corridorGlow" x1="0" y1="0" x2="0" y2="1">
          <stop offset="0" stop-color="var(--night)"/>
          <stop offset="0.35" stop-color="var(--corridor-mid)"/>
          <stop offset="0.6" stop-color="var(--corridor-light)"/>
          <stop offset="1" stop-color="var(--corridor-blue)"/>
        </linearGradient>
      </defs>
      <rect width="584" height="347" fill="url(#corridorGlow)"/>
    </svg>
    <h1 class="front-title">Lanterns<br>Over the Marsh<br>Gate</h1>
    <p class="front-subtitle">the quiet geography of tidal winds,<br>ferry routes and harbour lanterns</p>
    <p class="front-edition">2nd edition</p>
    <p class="front-author">Rupert Calloway</p>
  </section>
</div>
</body>
</html>
```